Epoxy Flooring Contractor business card

We need a business card to promote a new addition to our business. We now offer Epoxy Flooring. We would like for the business card to include the images attached. One is our logo, the other is a sample of metallic epoxy flooring, we would like to incorporate that somewhere into the design. I was thinking an icon of a man pushing a concrete grinder and have the color set to the metallic epoxy color. I found a business card sample on this website, I will attach it. It has the icon that we are looking for, or something similar.
Our company name is Brightmore Coatings LLC
Our owners name is Dana Pellow
Phone is 561-847-2916
website is www.brightmore-coatingsllc.com
please let me know if you need any other info

Contact Information for Business Card

Brightmore Coatings LLC
Dana Pellow, owner
Phone: 561-847-2916
Address: P.O Box 8146 Lake Worth, FL 33471
www.Brightmore-CoatingsLLC.com
BrightmoreCoatingsLLC@mailvista.net
Include logo attached
It must include a Clip art of man with concrete grinder
Must include metallic epoxy design attached
Must include the following text
Residential Garage Flooring
Epoxy Countertops
Commercial Epoxy Flooring
Restaurant Flooring
Warehouse Flooring
Licensed & Insured
Free Estimates

Colors

Designer to choose colors to be used in the design.

Requirements
Must have
• Include logo attached
• It must include a Clip art of man with concrete grinder
• Must include metallic epoxy design attached
• Must include the following text
• Garage Epoxy Flooring
• Residential Epoxy Flooring
• Concrete Floor Crack Repairs
• Concrete Floor Grinding
• Commercial & Warehouse Epoxy Flooring
• Restaurant Epoxy Flooring
• Epoxy Countertops
• Non Slip Epoxy Pool Decks
• Textured Finishes, Flakes, Granite Coat, Metallic & Quartz
• FREE ESTIMATES • LICENSED & INSURED

```html
<!DOCTYPE html>
<html lang="en">
<head>
<meta charset="utf-8">
<title>Brightmore Coatings LLC – Business Card</title>
<link rel="stylesheet" href="https://fonts.googleapis.com/css2?family=Montserrat:wght@500;600;700&family=Open+Sans:wght@400;600;700&display=swap">
<style>
  :root {
    --blue-deep: #3d6391;
    --blue-soft: #86a9d1;
    --blue-band: #7d9fca;
    --grey-dark: #4b4c4e;
    --grey-mid: #6e6f72;
    --grey-light: #e6e6e4;
    --ink: #2f3033;
    --paper: #ffffff;
    --backdrop: #d9dadc;
  }
  * { box-sizing: border-box; margin: 0; padding: 0; }
  html, body { width: 1200px; height: 1200px; overflow: hidden; background: var(--backdrop); }
  body { position: relative; font-family: "Open Sans", Arial, sans-serif; }

  .card {
    position: absolute; left: 120px; width: 960px; height: 548px;
    overflow: hidden; background: var(--paper);
    box-shadow: 0 6px 18px rgba(0,0,0,.18);
  }
  .card--services { top: 40px; }
  .card--contact  { top: 612px; }

  /* ---------- services side ---------- */
  .texture-dark {
    position: absolute; left: 0; width: 100%;
    background: radial-gradient(circle at 30% 40%, #5a5b5e, var(--grey-dark) 60%, #3c3d3f);
  }
  .texture-dark--top { top: 0; height: 96px; }
  .texture-dark--bottom { bottom: 0; height: 96px; }
  .rule { position: absolute; left: 0; width: 100%; background: var(--blue-deep); }
  .rule--a { top: 96px; height: 10px; }
  .rule--b { top: 260px; height: 10px; }
  .rule--c { bottom: 96px; height: 10px; }

  .brand-band {
    position: absolute; left: 0; top: 106px; width: 100%; height: 154px;
    background: var(--grey-light);
    display: flex; align-items: center; padding: 0 60px;
  }
  .wordmark { display: flex; align-items: center; gap: 18px; }
  .wordmark__square { width: 46px; height: 46px; background: var(--blue-soft); flex: none; }
  .wordmark__name {
    font-family: "Montserrat", Arial, sans-serif; font-weight: 600;
    font-size: 44px; line-height: 1; letter-spacing: 4px; color: var(--grey-mid);
    white-space: nowrap;
  }
  .wordmark__name span { display: block; }
  .brand-band__links { margin-left: auto; display: flex; align-items: center; gap: 14px; }
  .social-dot { width: 46px; height: 46px; border-radius: 50%; background: var(--blue-deep); }
  .phone-line {
    display: flex; align-items: center; gap: 8px; margin-left: 10px;
    font-size: 26px; color: var(--blue-deep);
  }
  .phone-line svg { width: 24px; height: 24px; fill: var(--blue-soft); }

  .services-band {
    position: absolute; left: 0; top: 270px; width: 100%; bottom: 106px;
    background: var(--blue-band);
    display: flex; flex-direction: column; justify-content: center;
    padding: 0 50px; text-align: center;
    color: var(--paper); font-weight: 700; font-size: 20px; line-height: 1.42;
  }
  .services-band .services-band__tag { margin-top: 2px; }

  /* ---------- contact side ---------- */
  .photo { position: absolute; }
  .photo--metallic {
    left: 0; top: 0; width: 420px; height: 300px;
    background: radial-gradient(ellipse at 40% 55%, #3a63b8, #2b3f6b 55%, #3a4149);
  }
  .photo--flake {
    left: 420px; top: 0; width: 540px; height: 112px;
    background: linear-gradient(120deg, #b9bcc2, #5e6168 45%, #a7abb2 70%, #2a2c31);
  }
  .contact-rule { position: absolute; background: var(--blue-deep); }
  .contact-rule--top { left: 420px; top: 112px; width: 540px; height: 8px; }
  .contact-rule--mid { left: 420px; top: 300px; width: 540px; height: 6px; }
  .contact-rule--low { left: 0; top: 470px; width: 100%; height: 10px; }

  .contact-brand { position: absolute; left: 446px; top: 168px; }
  .contact-brand .wordmark { gap: 14px; }
  .contact-brand .wordmark__square { width: 40px; height: 40px; background: var(--blue-deep); }
  .contact-brand .wordmark__name { font-size: 34px; letter-spacing: 3px; color: var(--grey-mid); }

  .grinder-figure {
    position: absolute; left: 808px; top: 136px; width: 126px; height: 148px;
    background: linear-gradient(180deg, #5677a4, var(--blue-deep));
    border-radius: 6px;
  }

  .contact-lines {
    position: absolute; left: 560px; top: 324px;
    font-size: 19px; color: var(--ink); line-height: 1.6;
  }
  .contact-lines li { list-style: none; display: flex; align-items: center; gap: 10px; white-space: nowrap; }
  .contact-lines svg { width: 18px; height: 18px; fill: var(--blue-deep); flex: none; }

  .person { position: absolute; left: 60px; top: 318px; }
  .person__name {
    font-family: "Montserrat", Arial, sans-serif; font-weight: 700;
    font-size: 38px; color: var(--blue-deep); letter-spacing: 1px; line-height: 1;
  }
  .person__role { font-size: 22px; color: var(--ink); margin-top: 4px; }
  .person__company { font-size: 22px; color: var(--blue-deep); margin-top: 8px; }
  .person__address { font-size: 22px; color: var(--ink); white-space: nowrap; }
</style>
</head>
<body>

<section class="card card--services">
  <div class="texture-dark texture-dark--top"></div>
  <div class="rule rule--a"></div>
  <div class="brand-band">
    <div class="wordmark">
      <div class="wordmark__square"></div>
      <div class="wordmark__name"><span>Brightmore</span><span>Coatings</span></div>
    </div>
    <div class="brand-band__links">
      <div class="social-dot"></div>
      <div class="social-dot"></div>
      <div class="phone-line">
        <svg viewBox="0 0 24 24"><path d="M6.6 10.8a15.1 15.1 0 0 0 6.6 6.6l2.2-2.2a1 1 0 0 1 1-.25 11.4 11.4 0 0 0 3.6.57 1 1 0 0 1 1 1V20a1 1 0 0 1-1 1A17 17 0 0 1 3 4a1 1 0 0 1 1-1h3.5a1 1 0 0 1 1 1c0 1.25.2 2.45.57 3.57a1 1 0 0 1-.25 1z"/></svg>
        561-847-2916
      </div>
    </div>
  </div>
  <div class="rule rule--b"></div>
  <div class="services-band">
    <p>Garage Epoxy Flooring, Residential Epoxy Flooring, Concrete Floor Crack Repairs, Concrete Floor Grinding, Commercial &amp; Warehouse Epoxy Flooring, Restaurant Epoxy Flooring, Restaurant Epoxy Flooring, Epoxy Countertops, Non Slip Epoxy Pool Decks, Textured Finishes, Flakes, Granite Coat, Metallic &amp; Quartz,</p>
    <p class="services-band__tag">FREE ESTIMATES , LICENSED &amp; INSURED</p>
  </div>
  <div class="rule rule--c"></div>
  <div class="texture-dark texture-dark--bottom"></div>
</section>

<section class="card card--contact">
  <div class="photo photo--metallic" role="img" aria-label="Blue metallic epoxy floor sample"></div>
  <div class="photo photo--flake" role="img" aria-label="Grey, black and blue flake epoxy floor sample"></div>
  <div class="contact-rule contact-rule--top"></div>

  <div class="contact-brand">
    <div class="wordmark">
      <div class="wordmark__square"></div>
      <div class="wordmark__name"><span>Brightmore</span><span>Coatings</span></div>
    </div>
  </div>
  <div class="grinder-figure" role="img" aria-label="Clip art of a worker pushing a concrete floor grinder"></div>
  <div class="contact-rule contact-rule--mid"></div>

  <ul class="contact-lines">
    <li><svg viewBox="0 0 24 24"><path d="M6.6 10.8a15.1 15.1 0 0 0 6.6 6.6l2.2-2.2a1 1 0 0 1 1-.25 11.4 11.4 0 0 0 3.6.57 1 1 0 0 1 1 1V20a1 1 0 0 1-1 1A17 17 0 0 1 3 4a1 1 0 0 1 1-1h3.5a1 1 0 0 1 1 1c0 1.25.2 2.45.57 3.57a1 1 0 0 1-.25 1z"/></svg>561 - 847 - 2916</li>
    <li><svg viewBox="0 0 24 24"><path d="M2 5h20v14H2z M2 5l10 8 10-8" stroke="#fff" stroke-width="1.5"/></svg>BrightmoreCoatingsLLC@mailvista.net</li>
    <li><svg viewBox="0 0 24 24"><circle cx="12" cy="12" r="10"/><path d="M2 12h20M12 2c3 3 3 17 0 20M12 2c-3 3-3 17 0 20" stroke="#fff" stroke-width="1.3" fill="none"/></svg>www.brightmore-coatingsllc.com</li>
  </ul>

  <div class="person">
    <div class="person__name">DANA PELLOW</div>
    <div class="person__role">owner</div>
    <div class="person__company">Brightmore Coatings LLC</div>
    <div class="person__address">P.O Box 8146 Lake Worth, FL 33471</div>
  </div>
  <div class="contact-rule contact-rule--low"></div>
</section>

</body>
</html>
```